Lawn Maintenance Company needs Flyer (Postcard) Design.

Hi everyone.
The majority of what I do is lawn maintenance (grass cutting and trimming/edging).

I'm pretty well open to anything (even humour) but want to stay away from the cartoon/illustration type flyer (but always receptive if you think you have something that might look good, like Pipkin (Thimbles character) :)
Simple but I guess as everyone, something that catches people's eye.

Feel free to kind of play with the name if you think it would help, I would be willing to pay extra if you thought you had a good idea for some type of logo also.

Flyer/Postcard will be front and back, front mainly outlined here, back would be a list of additional services.

Main points I want to get across.
- Professional
- Reliable
- Not like the larger companies that send students or part time
helpers
Kind of want to get those points across without necessarily saying them.

Ok, well, if you haven't rolled your eyes and headed off to the next project.................... :)

Target Market(s)

Mostly regular people with bungalow / two storey houses that don't want to do it themselves and want a nice lawn to frame their house.

Industry/Entity Type

It Company

Requirements
Must have
• Front
** Bramblecrest Landscaping and Lawn Services
** Lawn Maintenance
** (416) 555-3827
** bramblecrestyard@mailvora.com

Back
Commercial and Residential
Plaza Maintenance
Spring/Fall Clean-up
Fertilizing
Weed Prevention
Hedge Trimming
Flower Bed Design
Topdressing
Triplemix
Overseeding
Lawn & flower bed re-edging
Eavestrough Cleaning
Nice to have
• ummmm....grass. lol :)
Birds
Butterflies
Should not have
• Elaborate homes/gardens
Pictures/photos of people

**The pictures I have included are to just give you an idea of the work I do and the type of properties I do**
Please let me know if you want more pics.

```html
<!DOCTYPE html>
<html lang="en">
<head>
<meta charset="utf-8">
<title>Bramblecrest Landscaping and Lawn Services – What We Do</title>
<link rel="stylesheet" href="https://fonts.googleapis.com/css2?family=Kalam:wght@400;700&family=Fira+Sans:wght@600&display=swap">
<style>
  :root {
    --leaf-light: #eaf3c9;
    --leaf-mid: #b9dc6a;
    --leaf-deep: #6fb23a;
    --grass-top: #4f9a22;
    --grass-base: #1d5e0c;
    --title-green: #1c9a28;
    --maroon: #6a1616;
    --dot-green: #2fa52b;
    --haze: rgba(255, 255, 255, 0.75);
  }

  * { box-sizing: border-box; margin: 0; padding: 0; }

  html, body {
    width: 800px;
    height: 1200px;
    overflow: hidden;
    background: #ffffff;
  }

  .flyer-back {
    position: relative;
    width: 800px;
    height: 1200px;
    overflow: hidden;
  }

  .backdrop {
    position: absolute;
    inset: 0;
    background:
      radial-gradient(ellipse 260px 200px at 400px 230px, var(--haze), transparent 70%),
      radial-gradient(ellipse 200px 180px at 700px 520px, rgba(255,255,255,0.55), transparent 70%),
      radial-gradient(ellipse 240px 260px at 90px 360px, rgba(150, 205, 60, 0.55), transparent 70%),
      radial-gradient(ellipse 300px 260px at 640px 160px, rgba(210, 235, 150, 0.7), transparent 70%),
      linear-gradient(180deg, var(--leaf-light) 0%, var(--leaf-mid) 55%, var(--leaf-deep) 85%);
  }

  .grass {
    position: absolute;
    left: 0;
    right: 0;
    bottom: 0;
    height: 330px;
    background: linear-gradient(180deg,
      rgba(79, 154, 34, 0) 0%,
      var(--grass-top) 22%,
      #2f7a14 60%,
      var(--grass-base) 100%);
  }

  .services {
    position: absolute;
    top: 0;
    left: 0;
    width: 800px;
    text-align: center;
  }

  .services-title {
    position: absolute;
    top: 70px;
    left: 0;
    width: 800px;
    font-family: "Kalam", cursive;
    font-weight: 400;
    font-size: 48px;
    line-height: 60px;
    color: var(--title-green);
    letter-spacing: 1px;
  }

  .service-list {
    position: absolute;
    top: 172px;
    left: 0;
    width: 800px;
    list-style: none;
  }

  .service-line {
    height: 90.2px;
    line-height: 90px;
    font-family: "Fira Sans", sans-serif;
    font-weight: 600;
    font-size: 36px;
    color: var(--maroon);
    letter-spacing: -0.3px;
  }

  .dot {
    display: inline-block;
    width: 27px;
    height: 27px;
    margin: 0 8px;
    border-radius: 50%;
    background: var(--dot-green);
    vertical-align: -3px;
  }
</style>
</head>
<body>
  <main class="flyer-back">
    <div class="backdrop" role="img" aria-label="Soft out-of-focus photograph of sunlit green foliage"></div>
    <div class="grass" role="img" aria-label="Close-up photograph of tall green grass blades along the bottom edge"></div>

    <section class="services">
      <h1 class="services-title">what we do...</h1>
      <ul class="service-list">
        <li class="service-line">Commercial and Residential</li>
        <li class="service-line">Plaza Maintenance<span class="dot"></span>Spring/Fall</li>
        <li class="service-line">Clean-up<span class="dot"></span>Fertilizing<span class="dot"></span>Weed</li>
        <li class="service-line">Prevention<span class="dot"></span>Hedge Trimming</li>
        <li class="service-line">Flower Bed Design<span class="dot"></span>Topdressing</li>
        <li class="service-line">Triplemix<span class="dot"></span>Overseeding</li>
        <li class="service-line">Lawn &amp; flower bed re-edging</li>
        <li class="service-line">Eavestrough Cleaning</li>
      </ul>
    </section>
  </main>
</body>
</html>
```